Small Business Broker Business Card Design

A business card design for a small business brokerage, which is a financial service, not unlike real estate brokerage, but for small businesses such as laundromats, pizza shops, restaurants, cleaners etc. The designs should all be simple, more conservative in nature, using the colors and font of the logo. Again, think real estate Brokerage as a business context
Contact Information for Business Card
Name: Milo R. Dunbar. Title: Small Business Advisor. Email: m.dunbar@harborstoneadvisory.com. Mobile: (917) 555-0148. Office: (718) 555-0193. www.harborstoneadvisory.com

```html
<!DOCTYPE html>
<html lang="en">
<head>
<meta charset="utf-8">
<title>Harborstone Advisory – Business Card</title>
<link rel="stylesheet" href="https://fonts.googleapis.com/css2?family=Montserrat:wght@700;800&family=Arimo:ital,wght@0,400;0,700;1,400&display=swap">
<style>
  :root {
    --navy: #17315f;
    --green: #7bc12f;
    --ink-grey: #6f6f6f;
    --paper: #ffffff;
    --backdrop: #1c1c1c;
  }
  * { box-sizing: border-box; margin: 0; padding: 0; }
  html, body { width: 1200px; height: 963px; overflow: hidden; background: var(--backdrop); }
  .sheet { position: relative; width: 1200px; height: 963px; }

  .card {
    position: absolute;
    left: 250px;
    width: 700px;
    height: 400px;
    background: var(--paper);
    overflow: hidden;
  }
  .card--front { top: 58px; }
  .card--back { top: 505px; }

  /* Front */
  .header-band {
    position: absolute; left: 0; top: 0; width: 100%; height: 128px;
    background: var(--navy);
    border-bottom: 14px solid var(--green);
  }
  .person-name {
    position: absolute; left: 50px; top: 36px;
    font-family: "Montserrat", sans-serif; font-weight: 700;
    font-size: 31px; letter-spacing: 1px; text-transform: uppercase;
    color: var(--paper);
  }
  .person-title {
    position: absolute; left: 50px; top: 76px;
    font-family: "Arimo", sans-serif; font-size: 18px;
    color: var(--paper);
  }
  .contact-list {
    position: absolute; left: 50px; top: 184px;
    list-style: none;
    font-family: "Arimo", sans-serif; font-size: 17px; line-height: 27px;
    color: var(--ink-grey);
  }
  .contact-label { color: var(--green); font-weight: 700; margin-right: 6px; }

  .brand-lockup {
    position: absolute; right: 44px; bottom: 36px;
    text-align: left;
  }
  .brand-row { display: flex; align-items: center; gap: 10px; }
  .brand-square { width: 16px; height: 16px; background: var(--navy); }
  .brand-name {
    font-family: "Montserrat", sans-serif; font-weight: 800;
    font-size: 20px; letter-spacing: 1.5px; text-transform: uppercase;
    color: var(--navy);
  }
  .brand-tagline {
    margin-top: 5px;
    font-family: "Montserrat", sans-serif; font-weight: 700;
    font-size: 10px; letter-spacing: 1.6px; text-transform: uppercase;
    color: var(--green);
  }

  /* Back */
  .back-lockup {
    position: absolute; left: 0; top: 0; width: 100%; height: 100%;
    display: flex; flex-direction: column; align-items: center; justify-content: center;
  }
  .back-lockup .brand-name { font-size: 32px; letter-spacing: 2px; }
  .back-lockup .brand-tagline { font-size: 14px; letter-spacing: 2.4px; margin-top: 8px; }
</style>
</head>
<body>
<main class="sheet">
  <section class="card card--front">
    <div class="header-band"></div>
    <h1 class="person-name">Milo R. Dunbar</h1>
    <p class="person-title">Small Business Advisor</p>
    <ul class="contact-list">
      <li><span class="contact-label">O:</span>(718) 555-0193</li>
      <li><span class="contact-label">M:</span>(917) 555-0148</li>
      <li><span class="contact-label">E:</span>m.dunbar@harborstoneadvisory.com</li>
      <li>www.harborstoneadvisory.com</li>
    </ul>
    <div class="brand-lockup">
      <div class="brand-row">
        <span class="brand-square"></span>
        <span class="brand-name">Harborstone Advisory, Inc</span>
      </div>
      <p class="brand-tagline">Trusted guidance for every business sale</p>
    </div>
  </section>

  <section class="card card--back">
    <div class="back-lockup">
      <span class="brand-name">Harborstone Advisory, Inc</span>
      <p class="brand-tagline">Trusted guidance for every business sale</p>
    </div>
  </section>
</main>
</body>
</html>
```